Business Card Design for drone videography and photography

I have a Vorkel Skyra 3 drone. I am looking for a logo to somehow incorporate with my business name. I don't even know what is an appropriate font. I am most filming real estate homes. I want something simplistic and a logo that makes sense for the business that I'm in. xxxxxxxxxxxxxxxxxxxxxxxxxxxxxxxxxxxxxxxxxxxxxxxxxxxxxxxxxxxxxxxxxxxxxxxxxxxxxxxxxxxxxxxxxxxxxxxxxxxxxxxxxxxxxxxxxxxxxxxxxxxxxxxxxxxxxxxxxxxxxxxxxxxxxxxxxxxxxxxxxxxxxxxxxxxxxxxxxxxxxxxxxxxxxxxxxxxxxxxxxxxxxxxxxxxxxxxxxxxxxxxxxxxxxxxxxxxxxxxxxxxxxxxxxxxxxxxxxxxxxxxxxxxxxxxxxxxxxxxxxxxxxxxxxxxxxxxxxxxxxxxxxxxxxxxxxxxxxxxxxxxxxxxxxxxxxxxxxxxxxxxxxxxxxxxxxxxxxxxxxxxxxxxxxxxxxxxxxxxxxxxxxxxxxxxxxxxxxxxxxxxxxxxxxxxxxxxxxxxxxxxxxxxxxxxxxxxxxxxxxxxxxxxxxxxxxxxxxxxxxxxxxxxxxxxxxxxxxxxxxxxxxxxxxxxxxxxxxxxxxxxxxxxxxxxxxxxxxxxxxxxxxxxxxxxxxxxxxxxxxxxxxxxxxxxxxxxxxxxxxxxxxxxxxxxxxxxxxxxxxxxxxxxxxxxxxxxxxxxxxxxxxxxxxxxxxxxxxxxxxxxxxxxxxxxxxxxxxxxxxxxxxxxxxxxxxxxxxxxxxxxxxxxxxxxxxxxxxxxxxxxxxxxxxxxxxxxxxxxxxxxxxxxxxxxxxxxxxxxxxxxxxxxxxxxxxxxxxxxxxxxxxxxxxxxxxxxxxxxxxxxxxxxxxxxxxxxxxxxxxxxxxxxxxxxxxxxxxxxxxxxxxxxxxxxxxxxxxxxxxxxxxxxxxxxxxxxxxxxxxxxxxxxxxxxxxxxxxxxxxxxxxxxxxxxxxxxxxxxxxxxxxxxxxxxxxxxxxxxxxxxxxxxxxxxxxxxxxxxxxxxxxxxxxxxxxxxxxxxxxxxxxxxxxxxxxxxxxxxxxxxxxxxxxxxxxxxxxxxxxxxxxxxxxxxxxxxxxxxxxxxxxxxxxxxxxxxxxxxxxxxxxxxxxxxxxxxxxxxx

Target Market(s)

Real estate

Industry/Entity Type

Business

Contact Information for Business Card

TRASK AERIAL IMAGING
Daniel Trask
Owner/Operator

40528 Birchwood Ct.
Lindell Park IA 63514

314-555-0187
dtrask@traskaerialimaging.com

NAB Drone Certified
Insured
Section 333 Exempt
Vexo Flight Class Certified

Font styles to use
Other font styles liked:
• PUMP DEMI BOLD LET

Requirements
Must have
• Maybe have the certifications on the back??? The business card must be more serious than playful
Nice to have
• Possibly have the logo work itself into the business name?
Should not have
• nothing that looks like a "fun" business. I want this business card to look professional but also simplistic. I don't want a picture that I took from my drone as the background.

```html
<!DOCTYPE html>
<html lang="en">
<head>
<meta charset="UTF-8">
<title>Trask Aerial Imaging – Business Card</title>
<link href="https://fonts.googleapis.com/css2?family=PT+Sans+Narrow:wght@400;700&display=swap" rel="stylesheet">
<style>
  :root {
    --backdrop: #9c9fa3;
    --card-white: #ffffff;
    --band-grey: #e6e6e6;
    --charcoal: #2a2a2a;
    --sky: #00aeea;
    --sky-deep: #0097d8;
    --sky-shadow: #0a6db6;
    --text-dark: #3a3a3a;
    --text-light: #ffffff;
  }
  * { margin: 0; padding: 0; box-sizing: border-box; }
  html, body {
    width: 1200px; height: 861px; overflow: hidden;
    background: var(--backdrop);
    font-family: "PT Sans Narrow", "Arial Narrow", sans-serif;
  }
  .canvas { position: relative; width: 1200px; height: 861px; }

  .card {
    position: absolute; width: 604px; height: 356px; overflow: hidden;
    box-shadow: 0 4px 14px rgba(0,0,0,.25);
  }
  .card-front { left: 146px; top: 74px; background: var(--card-white); }
  .card-back  {
    left: 446px; top: 440px;
    background: linear-gradient(180deg, var(--sky) 0%, var(--sky-deep) 100%);
  }
  .card-art { position: absolute; inset: 0; }

  .brand {
    position: absolute; left: 56px; top: 92px;
    display: flex; align-items: center; gap: 8px;
    color: var(--charcoal); font-weight: 700; font-size: 24px; letter-spacing: 1px;
  }
  .brand-dot { width: 12px; height: 12px; border-radius: 50%; background: var(--sky); }

  .identity {
    position: absolute; right: 70px; top: 86px; text-align: right; color: var(--text-light);
  }
  .identity-name { font-weight: 700; font-size: 40px; line-height: 1; }
  .identity-role { font-size: 27px; line-height: 1.2; margin-top: 2px; }

  .contact {
    position: absolute; display: flex; align-items: center; gap: 12px; font-size: 16px;
    white-space: nowrap;
  }
  .contact svg { width: 15px; height: 15px; fill: var(--sky); flex: none; }
  .contact-phone { left: 40px; top: 238px; color: var(--text-dark); }
  .contact-email { left: 40px; top: 296px; color: var(--text-light); }
  .contact-address { left: 314px; top: 296px; color: var(--text-light); gap: 6px; font-size: 15px; }

  .credentials {
    position: absolute; left: 0; right: 0; top: 146px; text-align: center;
    color: var(--text-light); font-weight: 700; font-size: 20px; line-height: 1.3;
  }
  .back-name {
    position: absolute; left: 0; right: 0; top: 252px; text-align: center;
    color: var(--text-light); font-weight: 700; font-size: 17px; letter-spacing: .3px;
  }
</style>
</head>
<body>
<main class="canvas">

  <section class="card card-front" aria-label="Business card front">
    <svg class="card-art" viewBox="0 0 604 356" aria-hidden="true">
      <rect x="0" y="226" width="480" height="40" fill="var(--band-grey)"/>
      <path d="M604,36 L536,36 Q512,36 506,60 L462,236 Q454,266 424,266 L0,266 L0,356 L604,356 Z" fill="var(--charcoal)"/>
      <path d="M266,68 L604,68 L604,178 L250,178 Q236,178 240,166 L266,68 Z" fill="var(--sky)"/>
    </svg>

    <div class="brand"><span class="brand-dot"></span>TRASK AERIAL</div>

    <div class="identity">
      <div class="identity-name">Daniel Trask</div>
      <div class="identity-role">Owner/Operator</div>
    </div>

    <div class="contact contact-phone">
      <svg viewBox="0 0 24 24"><path d="M6.6 10.8a15.1 15.1 0 0 0 6.6 6.6l2.2-2.2c.3-.3.7-.4 1-.2 1.1.4 2.3.6 3.6.6.6 0 1 .4 1 1V20c0 .6-.4 1-1 1C10.6 21 3 13.4 3 4c0-.6.4-1 1-1h3.5c.6 0 1 .4 1 1 0 1.3.2 2.5.6 3.6.1.3 0 .7-.2 1z"/></svg>
      <span>314-555-0187</span>
    </div>
    <div class="contact contact-email">
      <svg viewBox="0 0 24 24"><path d="M2 9l10-6 10 6v11H2z M4 10l8 5 8-5"/></svg>
      <span>dtrask@traskaerialimaging.com</span>
    </div>
    <div class="contact contact-address">
      <svg viewBox="0 0 24 24"><path d="M12 2a7 7 0 0 0-7 7c0 5 7 13 7 13s7-8 7-13a7 7 0 0 0-7-7zm0 9.5A2.5 2.5 0 1 1 12 6.5a2.5 2.5 0 0 1 0 5z"/></svg>
      <span>40528 Birchwood Ct. Lindell Park IA 63514</span>
    </div>
  </section>

  <section class="card card-back" aria-label="Business card back">
    <svg class="card-art" viewBox="0 0 604 356" aria-hidden="true">
      <polygon points="150,146 548,146 498,218 100,218" fill="var(--sky-shadow)" stroke="var(--sky-shadow)" stroke-width="14" stroke-linejoin="round"/>
      <polygon points="150,140 548,140 498,212 100,212" fill="var(--charcoal)" stroke="var(--charcoal)" stroke-width="14" stroke-linejoin="round"/>
    </svg>
    <p class="credentials">NAB Drone Certified Insured Section 333<br>Exempt Vexo Flight Class Certified</p>
    <p class="back-name">TRASK AERIAL IMAGING</p>
  </section>

</main>
</body>
</html>
```